GRHLM 2026 Theme for Wall Banners

We need a design created for a wall banner 4 x 4 feet, for our church's 2026 Theme:
"Applying God's Word"
"Acquiring God's Wisdom"
"Acknowledging God's Will"
"Advancing God's Work"
Proverbs 3:5-6

Use the church's colors purple, silver, white and include the logo
Church Name: Grace-Rooted Harvest Church of Lake Meridian

Target Market(s)

Male & Female, ages 0-99

Industry/Entity Type

Religious, church

Colors
6B429C
8869AF
B7A5CE
E3DAEB
F3F0F8

Requirements
Must have
• Logo, colors, use of all 4 phrases; use of scripture text
Nice to have
• Maybe the phrases in / on pillars
Should not have
• Images or language that is non-Christian

```html
<!DOCTYPE html>
<html lang="en">
<head>
<meta charset="utf-8">
<title>GRHLM 2026 Theme Banner</title>
<link rel="stylesheet" href="https://fonts.googleapis.com/css2?family=Cinzel:wght@400;600;700;800&display=swap">
<style>
  :root {
    --purple-deep: #6b5190;
    --purple-brand: #6b429c;
    --purple-mid: #8869af;
    --purple-soft: #b7a5ce;
    --lavender: #e3daeb;
    --lavender-pale: #f3f0f8;
    --ink-dark: #2a1740;
    --white: #ffffff;
  }
  * { margin: 0; padding: 0; box-sizing: border-box; }
  html, body { width: 1200px; height: 1198px; overflow: hidden; }
  body {
    font-family: "Cinzel", serif;
    background: linear-gradient(180deg, var(--lavender) 0%, var(--lavender-pale) 100%);
    position: relative;
  }
  .banner { position: absolute; inset: 0; }
  .theme-panel {
    position: absolute; left: 0; top: 0; width: 1200px; height: 823px;
    background: var(--purple-deep);
    border-radius: 0 0 150px 150px;
    overflow: hidden;
  }
  .foliage {
    position: absolute;
    border-radius: 50%;
  }
  .foliage--panel-left {
    left: -60px; top: 440px; width: 380px; height: 360px;
    background: radial-gradient(ellipse at center, rgba(80,55,120,.55) 0%, rgba(80,55,120,0) 70%);
  }
  .foliage--panel-right {
    right: -40px; top: 320px; width: 420px; height: 420px;
    background: radial-gradient(ellipse at center, rgba(80,55,120,.55) 0%, rgba(80,55,120,0) 70%);
  }
  .foliage--lower-left {
    left: 20px; top: 850px; width: 360px; height: 320px;
    background: radial-gradient(ellipse at center, rgba(183,165,206,.6) 0%, rgba(183,165,206,0) 70%);
  }
  .foliage--lower-right {
    right: 20px; top: 850px; width: 360px; height: 320px;
    background: radial-gradient(ellipse at center, rgba(183,165,206,.6) 0%, rgba(183,165,206,0) 70%);
  }
  .church-title {
    position: absolute; left: 0; right: 0; top: 50px;
    text-align: center; color: var(--white);
    font-weight: 700; font-size: 29px; line-height: 40px; letter-spacing: .5px;
  }
  .pillar {
    position: absolute; width: 480px; text-align: center; color: var(--white);
  }
  .pillar--left { left: 25px; }
  .pillar--right { left: 660px; }
  .pillar--top { top: 155px; }
  .pillar--bottom { top: 370px; }
  .pillar__verb {
    display: block; font-weight: 800; font-size: 35px; line-height: 44px;
    text-shadow: -2px -2px 0 var(--ink-dark), 2px -2px 0 var(--ink-dark), -2px 2px 0 var(--ink-dark), 2px 2px 0 var(--ink-dark), 3px 3px 2px var(--ink-dark);
  }
  .pillar__object {
    display: block; font-weight: 600; font-size: 54px; line-height: 66px; letter-spacing: 1px;
  }
  .connectors { position: absolute; left: 0; top: 0; }
  .scripture-ref {
    position: absolute; left: 428px; top: 560px; width: 343px; height: 91px;
    display: flex; align-items: center; justify-content: center;
    color: var(--white); font-size: 30px; font-weight: 400;
  }
  .scripture-text {
    position: absolute; left: 0; right: 0; top: 690px;
    text-align: center; color: var(--white);
    font-weight: 700; font-size: 20px; line-height: 30px; letter-spacing: 1px;
  }
  .church-mark {
    position: absolute; left: 300px; top: 905px; width: 600px;
    display: flex; flex-direction: column; align-items: center; gap: 18px;
  }
  .church-mark__dot {
    width: 70px; height: 70px; border-radius: 50%; background: var(--purple-brand);
  }
  .church-mark__name {
    color: var(--purple-brand); font-weight: 700; font-size: 26px; line-height: 34px; text-align: center;
  }
</style>
</head>
<body>
<main class="banner">
  <section class="theme-panel">
    <div class="foliage foliage--panel-left" role="img" aria-label="Faint leafy branch with small blossoms"></div>
    <div class="foliage foliage--panel-right" role="img" aria-label="Faint leafy branch with small blossoms"></div>

    <h1 class="church-title">Grace-Rooted Harvest Church<br>of Lake Meridian</h1>

    <div class="pillar pillar--left pillar--top"><span class="pillar__verb">Applying</span><span class="pillar__object">God's Word</span></div>
    <div class="pillar pillar--right pillar--top"><span class="pillar__verb">Acquiring</span><span class="pillar__object">God's Wisdom</span></div>
    <div class="pillar pillar--left pillar--bottom"><span class="pillar__verb">Acknowledging</span><span class="pillar__object">God's Will</span></div>
    <div class="pillar pillar--right pillar--bottom"><span class="pillar__verb">Advancing</span><span class="pillar__object">God's Work</span></div>

    <svg class="connectors" width="1200" height="823" viewBox="0 0 1200 823" aria-hidden="true">
      <g fill="none" stroke="#ffffff" stroke-width="3">
        <polyline points="501,241 577,241 577,560"/>
        <polyline points="667,241 605,241 605,560"/>
        <polyline points="468,450 551,450 551,560"/>
        <polyline points="700,450 630,450 630,560"/>
        <rect x="429.5" y="561.5" width="340" height="88"/>
      </g>
    </svg>
    <div class="scripture-ref">Proverbs 3:5-6</div>

    <p class="scripture-text">Trust in the Lord with all your heart and lean not unto<br>your own understanding; in all your ways submit to him,<br>and he will make your paths straight.</p>
  </section>

  <div class="foliage foliage--lower-left" role="img" aria-label="Soft lavender leafy branch with blossoms"></div>
  <div class="foliage foliage--lower-right" role="img" aria-label="Soft lavender leafy branch with blossoms"></div>

  <div class="church-mark">
    <span class="church-mark__dot"></span>
    <span class="church-mark__name">Grace-Rooted Harvest Church<br>of Lake Meridian</span>
  </div>
</main>
</body>
</html>
```